BrightHaven Webpage for Integrative and Holistic Psychiatric Practice

We need a webpage designed for a medical practice that focuses on integrative and holistic psychiatry. We focus on providing care to mothers and families. The name of the company is Bright Haven, incorporated, A Professional Medical Corporation.

We'd like the color palette to be earthy/natural with the same look and feel as our logo that's attached. We're not set on anything, so feel free to have fun with the palette. We just want it to be warm and inviting in particular for Moms!

We'd like to have our logo in the top left with links below it either centered or to the right. We really like websites like http://www.maplerivercare.example/home.html and http://www.tarrowfieldclinicpartners.example/site/ to give you an idea of what we're looking for.

For links, we're looking for the following. Dummy text is fine, we're still getting content together:

* Home
* About Us - this page would have headings for Directions, Staff, Appointment Scheduling
* Services Provided - headings for 8 different services
* Patient Resources - headings for Patient Forms, Fees, Articles
* FAQ
* Contact Us

The webpage will be hosted as an Cloudvane 9 Public Website, so feel free to use whatever DeskLoom integration you would like, but it's not necessary.

Thank you!

```html
<!DOCTYPE html>
<html lang="en">
<head>
<meta charset="utf-8">
<title>BrightHaven – A Professional Medical Corporation</title>
<link href="https://fonts.googleapis.com/css2?family=Open+Sans:wght@300;400;600;700&display=swap" rel="stylesheet">
<style>
:root{
  --brown:#5b2e0e;
  --brown-frame:#6b3410;
  --green:#2d5e0a;
  --leaf:#4f8a1c;
  --ink:#1a1a1a;
  --nav:#141414;
  --nav-dark:#050505;
  --nav-text:#d8d8d8;
  --body-text:#6a6a6a;
  --field:#f1f1f1;
  --field-text:#a8a8a8;
  --page:#f6f6f6;
  --panel:#ffffff;
  --band:#f1f1f1;
  --sq-blue:#27b4e8;
  --sq-red:#d6322a;
  --sq-navy:#3b5a9a;
  --sq-gray:#7a7a7a;
}
*{box-sizing:border-box;margin:0;padding:0}
html,body{width:1086px;height:1200px;overflow:hidden}
body{background:var(--page);font-family:"Open Sans",Arial,sans-serif;position:relative;color:var(--body-text)}
.abs{position:absolute}

/* header */
.brand{left:152px;top:40px;display:flex;align-items:center;gap:10px}
.brand-mark{width:34px;height:34px;border-radius:50%;background:var(--leaf)}
.brand-name{font-size:24px;font-weight:600;color:var(--brown)}
.social{display:flex;gap:6px}
.social span{display:block;width:22px;height:22px;border-radius:2px}
.social .s1{background:var(--sq-blue)}
.social .s2{background:var(--sq-red)}
.social .s3{background:var(--sq-navy)}
.header-social{left:851px;top:17px}
.contact-line{right:153px;font-size:20px;font-weight:300;color:var(--brown);display:flex;align-items:center;gap:6px;white-space:nowrap}
.contact-line svg{display:block}
.phone{top:52px}
.email{top:86px}

/* nav */
.main-nav{left:156px;top:128px;width:777px;height:51px;background:var(--nav);border-radius:6px 6px 0 0;display:flex;align-items:center}
.nav-home{width:59px;height:51px;background:var(--nav-dark);border-radius:6px 0 0 0;border-bottom:4px solid var(--brown-frame);display:flex;align-items:center;justify-content:center}
.nav-links{display:flex;list-style:none;margin-left:45px}
.nav-links li{font-size:11px;color:var(--nav-text);text-transform:uppercase;margin-right:54px;letter-spacing:.2px}
.nav-search{position:absolute;right:0;top:0;width:59px;height:51px;background:var(--nav-dark);border-radius:0 6px 0 0;display:flex;align-items:center;justify-content:center}

/* hero */
.hero{left:156px;top:179px;width:777px;height:271px;border:5px solid var(--brown-frame);border-top-width:6px;overflow:hidden}
.hero-photo{position:absolute;inset:0;background:linear-gradient(90deg,#fbf1ec 0%,#f6ddd3 35%,#efc3b4 60%,#e9b8a8 80%,#c98e80 100%)}
.hero-title{position:absolute;left:22px;top:44px;font-size:37px;font-weight:300;color:var(--brown);line-height:44px;text-transform:uppercase}
.btn{border:1px solid var(--brown);background:#fff;color:var(--brown);font-weight:700;text-transform:uppercase;display:flex;align-items:center;justify-content:center;font-size:14px}
.hero-btn{position:absolute;left:23px;top:153px;width:226px;height:40px;background:transparent}
.dots{position:absolute;left:24px;top:214px;display:flex;gap:3px}
.dots span{width:9px;height:9px;background:#ddd}
.dots .on{background:var(--brown)}

/* content panel */
.panel{left:156px;top:450px;width:777px;height:628px;background:var(--panel);box-shadow:0 0 6px rgba(0,0,0,.08)}
.welcome{left:170px;top:484px;width:490px}
.welcome h2{font-size:27px;font-weight:700;color:var(--green);margin-bottom:8px}
.welcome p{font-size:11px;line-height:13px;margin-bottom:13px;color:var(--body-text)}
.request{left:684px;top:486px;width:240px}
.request h2{font-size:27px;font-weight:400;color:var(--brown);line-height:31px;text-transform:uppercase;margin-bottom:14px}
.field{width:235px;height:30px;background:var(--field);margin:0 0 3px 2px;font-size:10px;color:var(--field-text);text-transform:uppercase;padding:9px 10px;position:relative}
.field.tall{height:77px}
.field svg{position:absolute;right:8px;top:8px}
.send{width:96px;height:33px;margin:6px 0 0 2px;border-radius:4px}

/* services */
.services{left:156px;top:840px;width:777px;height:238px;background:var(--band)}
.services h2{position:absolute;left:0;width:100%;top:26px;text-align:center;font-size:25px;font-weight:700;color:var(--brown)}
.svc{position:absolute;top:75px;width:245px;height:143px}
.svc-1{left:12px;background:linear-gradient(135deg,#c98f63,#e6c09a 50%,#8a9a4a)}
.svc-2{left:266px;background:linear-gradient(135deg,#8b6242,#a27b57 60%,#b08b66)}
.svc-3{left:520px;background:linear-gradient(180deg,#9fc1e2 0%,#dfeaf3 50%,#c6b49c 80%,#9c8a72 100%)}
.svc-overlay{position:absolute;inset:0;display:flex;flex-direction:column;align-items:center;justify-content:center;color:#fff}
.svc-overlay h3{font-size:14px;font-weight:700;margin-bottom:9px;text-transform:uppercase}
.view-more{background:#fff;color:var(--green);font-size:11px;font-weight:700;padding:6px 8px;border-radius:2px;text-transform:uppercase}

/* footer */
.footer-brand{left:0;width:1086px;top:1108px;display:flex;justify-content:center;align-items:center;gap:6px}
.footer-brand .brand-mark{width:18px;height:18px}
.footer-brand .brand-name{font-size:15px}
.copyright{left:0;width:1086px;top:1149px;text-align:center;font-size:9px;text-transform:uppercase;color:#666}
.footer-social{left:504px;top:1166px}
.footer-social .s2,.footer-social .s3{background:var(--sq-gray)}
</style>
</head>
<body>

<header>
  <div class="abs brand"><span class="brand-mark"></span><span class="brand-name">BrightHaven</span></div>
  <div class="abs social header-social"><span class="s1"></span><span class="s2"></span><span class="s3"></span></div>
  <div class="abs contact-line phone">
    <svg width="20" height="20" viewBox="0 0 20 20"><path d="M5 2l3 4-2 2c1 3 3 5 6 6l2-2 4 3-2 3C9 18 2 11 2 4z" fill="none" stroke="#5b2e0e" stroke-width="1.8"/></svg>
    10 20 30 40 50
  </div>
  <div class="abs contact-line email">
    <svg width="24" height="18" viewBox="0 0 24 18"><rect x="1" y="1" width="22" height="16" fill="none" stroke="#5b2e0e" stroke-width="2"/><path d="M1 1l11 9 11-9" fill="none" stroke="#5b2e0e" stroke-width="2"/></svg>
    info@brighthaven.example
  </div>
</header>

<nav class="abs main-nav">
  <div class="nav-home">
    <svg width="24" height="20" viewBox="0 0 24 20"><path d="M12 1L1 11h3v8h6v-5h4v5h6v-8h3z" fill="#7a3c10"/></svg>
  </div>
  <ul class="nav-links">
    <li>About Us</li>
    <li>Services Provided</li>
    <li>Patient Resources</li>
    <li>FAQ</li>
    <li>Contact Us</li>
  </ul>
  <div class="nav-search">
    <svg width="22" height="22" viewBox="0 0 22 22"><circle cx="9" cy="9" r="7" fill="none" stroke="#7a3c10" stroke-width="2"/><path d="M14 14l6 6" stroke="#7a3c10" stroke-width="2.5"/></svg>
  </div>
</nav>

<section class="abs hero">
  <div class="hero-photo" role="img" aria-label="Warm close-up photo of hands shaping a heart in soft pink light"></div>
  <h1 class="hero-title">A Professional<br>Medical Corporation</h1>
  <div class="btn hero-btn">Make Appointment</div>
  <div class="dots"><span></span><span></span><span></span><span class="on"></span><span></span></div>
</section>

<div class="abs panel"></div>

<section class="abs welcome">
  <h2>WELCOME</h2>
  <p>Lorem ipsum dolor sit amet, consectetuer adipiscing elit, sed diam nonummy nibh euismod tincidunt ut laoreet dolore magna aliquam erat volutpat.</p>
  <p>Ut wisi enim ad minim veniam, quis nostrud exerci tation ullamcorper suscipit lobortis nisl ut aliquip ex ea commodo consequat.</p>
  <p>Duis autem vel eum iriure dolor in hendrerit in vulputate velit esse molestie consequat, vel illum dolore eu feugiat nulla facilisis at vero eros et accumsan et iusto odio dignissim qui blandit praesent luptatum zzril delenit augue duis dolore te feugait nulla facilisi.Lorem ipsum dolor sit amet, consectetuer adipiscing elit, sed diam nonummy nibh euismod tincidunt ut laoreet dolore magna aliquam erat volutpat.</p>
  <p>Ut wisi enim ad minim veniam, quis nostrud exerci tation ullamcorper suscipit lobortis nisl ut aliquip ex ea commodo consequat.</p>
  <p>Duis autem vel eum iriure dolor in hendrerit in vulputate velit esse molestie consequat, vel illum dolore eu feugiat nulla facilisis at vero eros et accumsan et iusto odio dignissim qui blandit praesent luptatum zzril delenit augue duis dolore te feugait nulla facilisi.</p>
</section>

<section class="abs request">
  <h2>Request an<br>Appointment</h2>
  <div class="field">Your Name*
    <svg width="14" height="14" viewBox="0 0 14 14"><circle cx="7" cy="4" r="3" fill="#cfcfcf"/><path d="M1 14c0-4 3-6 6-6s6 2 6 6z" fill="#cfcfcf"/></svg></div>
  <div class="field">Your Email*
    <svg width="16" height="12" viewBox="0 0 16 12"><rect x="1" y="1" width="14" height="10" fill="none" stroke="#cfcfcf"/><path d="M1 1l7 6 7-6" fill="none" stroke="#cfcfcf"/></svg></div>
  <div class="field">Your Phone Number*
    <svg width="14" height="14" viewBox="0 0 20 20"><path d="M5 2l3 4-2 2c1 3 3 5 6 6l2-2 4 3-2 3C9 18 2 11 2 4z" fill="none" stroke="#cfcfcf" stroke-width="2"/></svg></div>
  <div class="field">Subject</div>
  <div class="field tall">Your Message
    <svg width="16" height="14" viewBox="0 0 16 14"><path d="M1 1h14v9H6l-3 3v-3H1z" fill="#cfcfcf"/></svg></div>
  <div class="btn send">Send</div>
</section>

<section class="abs services">
  <h2>SERVICES PROVIDED</h2>
  <div class="svc svc-1" role="img" aria-label="Photo of a smiling family of four together outdoors"></div>
  <div class="svc svc-2" role="img" aria-label="Photo of a counselling session in a warm room">
    <div class="svc-overlay"><h3>Lorem Ipsum Dolor</h3><span class="view-more">View More</span></div>
  </div>
  <div class="svc svc-3" role="img" aria-label="Photo of a family walking hand in hand on a beach"></div>
</section>

<footer>
  <div class="abs footer-brand"><span class="brand-mark"></span><span class="brand-name">BrightHaven</span></div>
  <div class="abs copyright">Copyright © 2014 Bright Haven Inc.</div>
  <div class="abs social footer-social"><span class="s1"></span><span class="s2"></span><span class="s3"></span></div>
</footer>

</body>
</html>
```